Bold Ladies - Fitness Retreat

Tri Fold Brochure & Double sided A4 version options, see attached mockup.

Target Market: Women 18-50, Asian mainly .

Corala Fitness Presents - Bold Ladies Fitness Retreats:

Something communicating the spirit of getting fit, being strong, eating healthy and strong sense of the feminine.

Industry/Entity Type

Fitness

```html
<!DOCTYPE html>
<html lang="en">
<head>
<meta charset="utf-8">
<title>Bold Ladies Boot Camp – Brochure Spread</title>
<link href="https://fonts.googleapis.com/css2?family=Russo+One&family=Open+Sans:wght@400;600;700&display=swap" rel="stylesheet">
<style>
  :root {
    --page-bg: #d9d9d9;
    --white: #ffffff;
    --accent-red: #e0301e;
    --link-orange: #ff6a1a;
    --band-black: #111111;
  }
  * { margin: 0; padding: 0; box-sizing: border-box; }
  html, body { width: 1200px; height: 598px; overflow: hidden; background: var(--page-bg); }
  .brochure-spread {
    position: absolute; left: 217px; top: 29px; width: 765px; height: 540px;
    overflow: hidden; font-family: "Open Sans", Arial, sans-serif;
  }
  .spread-art { position: absolute; inset: 0; }
  .terms {
    position: absolute; left: 18px; top: 40px; width: 224px; color: var(--white);
  }
  .terms-title {
    font-family: "Russo One", sans-serif; font-style: italic; font-weight: 400;
    font-size: 13.5px; letter-spacing: 0.6px; margin-bottom: 5px;
  }
  .terms-list { list-style: none; font-size: 8.1px; line-height: 1.42; }
  .terms-list li { position: relative; padding-left: 9px; }
  .terms-list li::before {
    content: "✓"; position: absolute; left: 0; top: 0; font-size: 7.5px;
  }
  .further-info {
    position: absolute; left: 392px; top: 254px; width: 113px;
    color: var(--white); font-size: 7.8px; line-height: 1.4; text-align: right;
  }
  .further-info-title {
    font-family: "Russo One", sans-serif; font-weight: 400; color: var(--link-orange);
    font-size: 10px; letter-spacing: 0.8px; margin-bottom: 8px;
  }
  .further-info .gap { height: 11px; }
  .further-info .value { color: var(--link-orange); }
  .web-address {
    position: absolute; left: 402px; top: 451px; transform: translate(-50%, -50%) rotate(-34deg);
    font-family: "Russo One", sans-serif; font-size: 17px; color: var(--white);
    letter-spacing: 1px; white-space: nowrap;
  }
  .cover-title {
    position: absolute; left: 622px; top: 418px; transform: translate(-50%, -50%) rotate(-31deg);
    font-family: "Russo One", sans-serif; font-weight: 400; font-size: 28px; line-height: 1.15;
    color: var(--white); white-space: nowrap;
    text-shadow: 1px 2px 2px rgba(0,0,0,0.6);
  }
  .brand-mark {
    position: absolute; right: 14px; top: 24px; display: flex; align-items: center; gap: 6px;
    font-family: "Russo One", sans-serif; font-size: 13px; color: var(--white); letter-spacing: 0.5px;
  }
  .brand-mark .brand-square { width: 13px; height: 13px; background: var(--accent-red); }
</style>
</head>
<body>
<main class="brochure-spread">
  <svg class="spread-art" width="765" height="540" viewBox="0 0 765 540" xmlns="http://www.w3.org/2000/svg">
    <defs>
      <linearGradient id="plateSheen" x1="0" y1="0" x2="1" y2="1">
        <stop offset="0" stop-color="#7a0c0c"/>
        <stop offset="0.28" stop-color="#a81818"/>
        <stop offset="0.5" stop-color="#680909"/>
        <stop offset="0.72" stop-color="#a01616"/>
        <stop offset="1" stop-color="#560707"/>
      </linearGradient>
      <linearGradient id="termsSheen" x1="0" y1="0" x2="1" y2="1">
        <stop offset="0" stop-color="#5e0909"/>
        <stop offset="0.5" stop-color="#3e0505"/>
        <stop offset="1" stop-color="#5a0808"/>
      </linearGradient>
      <linearGradient id="boxingTone" x1="0" y1="0" x2="1" y2="1">
        <stop offset="0" stop-color="#b8301a"/>
        <stop offset="0.35" stop-color="#f0703c"/>
        <stop offset="0.6" stop-color="#e04a28"/>
        <stop offset="1" stop-color="#8a1a0e"/>
      </linearGradient>
      <radialGradient id="boxingGlow" cx="0.45" cy="0.35" r="0.5">
        <stop offset="0" stop-color="#ffb07a" stop-opacity="0.6"/>
        <stop offset="1" stop-color="#ffb07a" stop-opacity="0"/>
      </radialGradient>
      <linearGradient id="beachTone" x1="0" y1="0" x2="1" y2="1">
        <stop offset="0" stop-color="#77716c"/>
        <stop offset="0.5" stop-color="#514c48"/>
        <stop offset="1" stop-color="#2a2725"/>
      </linearGradient>
      <radialGradient id="beachWarm" cx="0.5" cy="0.55" r="0.5">
        <stop offset="0" stop-color="#c08c6a" stop-opacity="0.45"/>
        <stop offset="1" stop-color="#c08c6a" stop-opacity="0"/>
      </radialGradient>
      <linearGradient id="gardenTone" x1="0" y1="0" x2="0.3" y2="1">
        <stop offset="0" stop-color="#cfe6f2"/>
        <stop offset="0.18" stop-color="#93c3dd"/>
        <stop offset="0.34" stop-color="#5d8c3a"/>
        <stop offset="0.5" stop-color="#c48a60"/>
        <stop offset="0.6" stop-color="#c8403c"/>
        <stop offset="0.78" stop-color="#6f9148"/>
        <stop offset="1" stop-color="#4a7429"/>
      </linearGradient>
      <linearGradient id="insetTone" x1="0" y1="0" x2="1" y2="1">
        <stop offset="0" stop-color="#6e9a44"/>
        <stop offset="0.45" stop-color="#c99372"/>
        <stop offset="0.7" stop-color="#9fa6d8"/>
        <stop offset="1" stop-color="#4d7a2c"/>
      </linearGradient>
    </defs>

    <rect class="plate-background" width="765" height="540" fill="url(#plateSheen)"/>

    <polygon class="terms-panel" points="0,0 268,0 268,244 0,386" fill="url(#termsSheen)"/>
    <polygon class="terms-frame" points="11,34 245,34 245,233 11,362" fill="none" stroke="#ffffff" stroke-width="2.5"/>

    <g class="photo-boxing" role="img" aria-label="Photo: women training with boxing gloves, orange tint">
      <polygon points="268,0 512,0 512,112 268,240" fill="url(#boxingTone)"/>
      <polygon points="268,0 512,0 512,112 268,240" fill="url(#boxingGlow)"/>
    </g>

    <g class="photo-beach" role="img" aria-label="Photo: women doing leg raises on a dark sand beach">
      <polygon points="0,396 400,186 400,195 252,540 0,540" fill="url(#beachTone)"/>
      <polygon points="0,396 400,186 400,195 252,540 0,540" fill="url(#beachWarm)"/>
    </g>

    <line class="stripe-black" x1="0" y1="386" x2="512" y2="116" stroke="#111111" stroke-width="7"/>
    <line class="stripe-white" x1="0" y1="394" x2="512" y2="124" stroke="#ffffff" stroke-width="3.5"/>

    <polygon class="band-black" points="256,540 400,195 400,186 512,127 512,396 306,540" fill="#111111"/>
    <line class="stripe-white" x1="250" y1="540" x2="398" y2="193" stroke="#ffffff" stroke-width="3"/>

    <g class="photo-garden" role="img" aria-label="Photo: women doing boot camp drills in a tropical garden">
      <polygon points="512,0 765,0 765,200 512,332" fill="url(#gardenTone)"/>
    </g>
    <line class="stripe-black" x1="512" y1="343" x2="765" y2="211" stroke="#111111" stroke-width="16"/>
    <line class="stripe-white" x1="512" y1="357" x2="765" y2="225" stroke="#ffffff" stroke-width="4"/>
    <line class="stripe-white" x1="690" y1="540" x2="765" y2="498" stroke="#ffffff" stroke-width="6"/>

    <g class="inset-photo" transform="rotate(-25 450 171)">
      <rect x="388" y="116" width="124" height="110" fill="url(#insetTone)" stroke="#e0301e" stroke-width="4"
        role="img" aria-label="Photo: partner sparring practice outdoors"/>
    </g>
    <g class="inset-photo" transform="rotate(-25 601 262)">
      <rect x="536" y="204" width="130" height="116" fill="url(#insetTone)" stroke="#e0301e" stroke-width="4"
        role="img" aria-label="Photo: boxing pad work on the lawn"/>
    </g>
  </svg>

  <section class="terms">
    <h2 class="terms-title">TERMS AND CONDITIONS</h2>
    <ul class="terms-list">
      <li>Travel Insurance is mandatory for all of our guests</li>
      <li>Please confirm any special dietary needs before booking. Please note that for reasons of safety we cannot take guests who have a fatal allergy to any food/food groups. We are unable to provide separate meals and are very aware that the closest hospital may be up to 2 hours away.</li>
      <li>All clients to complete a Fitness &amp; Health Assessment from Trainer and to be completed prior to booking.</li>
      <li>Installment Payment is possible</li>
      <li>To secure your retreat we require a non-refundable deposit of $500pp</li>
      <li>Final payment to be made 30 days prior to arrival date. Cancellation fees may apply</li>
      <li>All funds are non-refundable if a guest chooses to cancel within 30 days of retreat start date.</li>
      <li>Refunds/credits will not be given after journey commencement, even if services, activities or meals are unused or cancelled for any reason</li>
      <li>Personal expenses to be paid in cash at end of retreat (laundry, drinks etc)</li>
      <li>We operate rain, hail or shine!</li>
    </ul>
  </section>

  <section class="further-info">
    <h3 class="further-info-title">FURTHER INFO:</h3>
    <p>MARISA</p>
    <p>+62 812.0456.7120</p>
    <p>marisa.coralafitness@mail.com</p>
    <p>www.corala-fitness.com</p>
    <div class="gap"></div>
    <p>Email : <span class="value">info@islandshare.com</span></p>
    <p>Mob : <span class="value">+62 812 4408 7726</span></p>
    <p>Web : <span class="value">www.islandshare.com</span></p>
  </section>

  <div class="web-address">www.corala-fitness.com</div>

  <h1 class="cover-title">BOLD LADIES<br>BOOT CAMP<br>BALI RETREATS</h1>

  <div class="brand-mark"><span class="brand-square"></span>CORALA FITNESS</div>
</main>
</body>
</html>
```